Australian Recruitment Agency Flyer

We are looking for a 1 page flyer to promote our recruitment company. We would like this to have a corporate look.

Attached is a word document with the content we would like included in the flyer.

I have also attached some of our clients logos to be included in the flyer

Target Market(s)

Professional organisations looking to hire new staff

Industry/Entity Type

It Company

Colors
85abd2
3176b5
31b7a3
d2a4cc
e667a6
b768aa
876aae
3276b5
f04a50

Requirements
Must have
• Must have the content that we have include on a word document in the design brief.

```html
<!DOCTYPE html>
<html lang="en">
<head>
<meta charset="utf-8">
<title>TalentBridge Recruitment Banner</title>
<link href="https://fonts.googleapis.com/css2?family=Source+Sans+3:wght@400;600;700&display=swap" rel="stylesheet">
<style>
  :root{
    --lime:#7dc21e;
    --lime-soft:rgba(125,194,30,.78);
    --forest:#2a8a2e;
    --ink:#1b1b1b;
    --navy:#2c3a57;
    --yellow:#f4e600;
    --white:#ffffff;
    --page:#f2f2f2;
  }
  *{box-sizing:border-box;margin:0;padding:0}
  html,body{width:1199px;height:1200px;overflow:hidden;background:var(--page);font-family:"Source Sans 3",Arial,sans-serif;color:var(--ink)}
  .banner{position:absolute;left:316px;top:1px;width:567px;height:1198px;background:var(--white);overflow:hidden}
  .hero{position:absolute;left:0;top:0;width:567px;height:790px}
  .brand{position:absolute;left:276px;top:40px;display:flex;align-items:center;gap:10px}
  .brand-mark{width:52px;height:52px;background:#6a3d9a;border-radius:50%}
  .brand-name{font-size:34px;font-weight:700;color:var(--navy);line-height:1;letter-spacing:-.5px}
  .brand-tag{font-size:11px;font-weight:600;color:var(--navy);margin-top:4px}
  .hero-copy{position:absolute;left:22px;top:538px;color:var(--white);font-size:20px;line-height:26px}
  .hero-copy .highlight{color:var(--yellow);font-weight:700;font-size:21px;display:block;margin:4px 0}
  .services{position:absolute;left:0;top:805px;width:567px}
  .row{position:absolute;left:0;width:567px}
  .row-label{position:absolute;width:170px;text-align:center;font-weight:700;font-size:14px;text-transform:uppercase}
  .icon{position:absolute;width:50px;height:50px;border-radius:50%;background:var(--lime);display:flex;align-items:center;justify-content:center}
  .copy{position:absolute;left:204px;font-size:8.5px;line-height:15px;color:var(--ink)}
  .logo-strip{position:absolute;left:0;top:1114px;width:565px;height:84px;background:var(--lime)}
  .client{position:absolute;background:var(--white);display:flex;align-items:center;justify-content:center;font-size:11px;font-weight:700;color:var(--ink)}
  .client.bare{background:none}
</style>
</head>
<body>
<main class="banner">
  <svg class="hero" viewBox="0 0 567 790" width="567" height="790">
    <defs>
      <linearGradient id="skyline" x1="0" y1="0" x2="0" y2="1">
        <stop offset="0" stop-color="#1c2a4a"/>
        <stop offset=".45" stop-color="#6b3a2e"/>
        <stop offset=".65" stop-color="#3a3238"/>
        <stop offset="1" stop-color="#5a4a2a"/>
      </linearGradient>
    </defs>
    <polygon role="img" aria-label="Photograph of a city skyline with illuminated towers at dusk" fill="url(#skyline)" points="0,73 408,303 567,298 567,503 138,790 0,790"/>
    <polygon fill="var(--lime)" points="0,0 468,268 408,303 0,73"/>
    <polygon fill="var(--forest)" points="408,303 567,215 567,298"/>
    <polygon fill="var(--lime-soft)" points="0,400 380,612 138,790 0,790"/>
    <polygon fill="var(--forest)" points="0,690 150,790 0,790"/>
    <polygon fill="var(--lime)" points="138,790 567,503 567,575 195,790"/>
    <polygon fill="var(--forest)" points="378,686 567,575 567,790"/>
  </svg>

  <div class="brand">
    <span class="brand-mark"></span>
    <div>
      <div class="brand-name">TalentBridge</div>
      <div class="brand-tag">Human Resources &amp; Recruitment</div>
    </div>
  </div>

  <p class="hero-copy">We have over<span class="highlight">20 YEARS OF EXPERIENCE</span>Helping companies hire<br>amazing talent</p>

  <section class="services">
    <div class="row" style="top:0">
      <div class="icon" style="left:53px;top:8px">
        <svg width="26" height="26" viewBox="0 0 26 26" fill="none" stroke="#fff" stroke-width="3" stroke-linecap="round"><line x1="4" y1="4" x2="22" y2="22"/><line x1="22" y1="4" x2="4" y2="22"/></svg>
      </div>
      <div class="row-label" style="left:-4px;top:70px">What we do</div>
      <p class="copy" style="top:20px">We aren't a recruitment agency, we are an extension of your team.<br>We become your very own HR &amp; Recruitment department to be called<br>&nbsp;upon as and when needed.</p>
    </div>
    <div class="row" style="top:104px">
      <div class="icon" style="left:49px;top:7px">
        <svg width="26" height="24" viewBox="0 0 26 24" fill="#fff"><rect x="2" y="14" width="4" height="9"/><rect x="8" y="10" width="4" height="13"/><rect x="14" y="12" width="4" height="11"/><rect x="20" y="6" width="4" height="17"/><polyline points="2,10 9,4 15,8 24,1" fill="none" stroke="#fff" stroke-width="2"/></svg>
      </div>
      <div class="row-label" style="left:2px;top:69px;width:180px">Industries we serve</div>
      <p class="copy" style="top:8px">Mining and Oil &amp; Gas<br>Accounting &amp; Finance<br>Sales &amp; Marketing<br>IT &amp; Communications<br>Government &amp; Not for Profit</p>
      <p class="copy" style="left:361px;top:19px">Start a conversation today<br>&nbsp;and see why these companies<br>&nbsp;turn to us time and time again</p>
    </div>
    <div class="row" style="top:206px">
      <div class="icon" style="left:46px;top:6px">
        <svg width="26" height="24" viewBox="0 0 26 24" fill="#fff"><rect x="2" y="11" width="5" height="11"/><path d="M9 11 L14 2 Q17 2 16 8 L23 8 Q25 9 24 12 L21 22 L9 22 Z"/></svg>
      </div>
      <div class="row-label" style="left:-13px;top:70px">Feedback</div>
      <p class="copy" style="top:10px">"TalentBridge really delivered on their promise and far exceeded our expectations.</p>
      <p class="copy" style="left:274px;top:36px">Their fixed fee model saved us thousands"</p>
      <p class="copy" style="top:64px">Mark Ellison General Manager<br>Harbour Financial Group</p>
    </div>
  </section>

  <section class="logo-strip" aria-label="Client list">
    <div class="client" style="left:58px;top:15px;width:68px;height:24px">Fleetly</div>
    <div class="client bare" style="left:184px;top:14px;width:64px;height:24px">Cobalt Ridge</div>
    <div class="client" style="left:294px;top:11px;width:46px;height:24px">Harbour</div>
    <div class="client" style="left:408px;top:14px;width:42px;height:26px">Zentra</div>
    <div class="client" style="left:147px;top:44px;width:36px;height:34px;font-size:7px">Kestrel</div>
    <div class="client" style="left:247px;top:44px;width:36px;height:34px;font-size:9px">Arcline</div>
    <div class="client bare" style="left:344px;top:48px;width:56px;height:30px;font-size:10px">Northwind</div>
  </section>
</main>
</body>
</html>
```